I am a Financial Adviser specialising in Aged Care Advice. We provide financial advice and assistance to families with loved ones entering an Aged Care facility.
We need a flyer detailing the Aged Care Packages that we offer. There will be 3 main packages & then other add ons. I need an area where the client can sign off on the package/s that they choose. I have attached a sample to demonstrate the required layout, and a copy of content. I would like the flyer to have an image as per the attached sample, and to be designed in soft pastels, blues, greens.

Financial

```html
<!DOCTYPE html>
<html lang="en">
<head>
<meta charset="utf-8">
<title>Aged Care Packages Flyer</title>
<link href="https://fonts.googleapis.com/css2?family=Roboto+Condensed:ital,wght@0,300;0,400;0,700;1,300&display=swap" rel="stylesheet">
<style>
:root{
  --backdrop:#e7e4de;
  --cream:#d8d6a8;
  --olive:#8a8a58;
  --olive-dark:#4f4f2c;
  --violet:#8e91bb;
  --violet-light:#aeb1d2;
  --violet-deep:#3c3f8c;
  --grey-band:#e6e6e8;
  --ink:#333;
  --white:#fff;
}
*{margin:0;padding:0;box-sizing:border-box}
html,body{width:1200px;height:1200px;overflow:hidden;background:var(--backdrop);font-family:"Roboto Condensed",sans-serif;color:var(--ink)}
.canvas{position:relative;width:1200px;height:1200px}
.page{position:absolute;top:253px;height:694px;overflow:hidden;box-shadow:0 6px 18px rgba(0,0,0,.18)}

/* options page */
.options{left:40px;width:532px;background:var(--white)}
.options__top{position:absolute;left:0;top:0;width:532px;height:473px;background:radial-gradient(ellipse at 55% 45%,#eeecd0 0%,var(--cream) 55%,#c9c78f 100%)}
.options__title{position:absolute;top:28px;width:100%;text-align:center;font-weight:700;font-size:29px;color:var(--olive-dark);letter-spacing:.3px}
.option{position:absolute;left:33px;width:477px;height:49px}
.option svg{position:absolute;left:0;top:0;width:100%;height:100%;display:block}
.option__label{position:absolute;left:0;top:0;width:125px;height:49px;display:flex;flex-direction:column;justify-content:center;align-items:center;text-align:center;color:var(--white);font-weight:700;font-size:9.5px;line-height:1.2}
.option__price{font-size:18px;line-height:1.15}
.option__text{position:absolute;left:166px;right:20px;top:0;height:49px;display:flex;align-items:center;color:var(--white);font-size:9.2px;line-height:1.35;font-weight:300;text-align:justify}
.signoff{position:absolute;left:33px;right:22px;top:484px;font-size:7px;line-height:1.4;color:#222}
.sig-row{position:absolute;font-size:9px;color:#222}
.dots{position:absolute;font-size:8px;color:#555;letter-spacing:.5px}
.disclaimer{position:absolute;left:33px;right:22px;top:610px;font-size:6.9px;line-height:1.4;color:#222}
.disclaimer p+p{margin-top:3px}
.options__foot{position:absolute;left:0;bottom:0;width:100%;height:23px;background:var(--cream)}

/* packages page */
.packages{left:623px;width:537px;background:var(--white)}
.packages__bg{position:absolute;left:0;top:0;width:100%;height:100%}
.photo{position:absolute}
.package{position:absolute;left:26px}
.package__name{font-weight:700;font-size:17px;color:var(--violet-deep)}
.package__tag{font-weight:300;font-size:13px;color:var(--violet-deep);margin-top:-2px}
.package__base{font-weight:700;font-size:11px;color:var(--white);margin-bottom:2px}
.package__list{list-style:none;font-size:9.3px;font-weight:300;color:var(--white);line-height:1.5}
.package__list li{padding-left:13px;position:relative}
.package__list li::before{content:"";position:absolute;left:0;top:4px;width:5px;height:5px;background:var(--white)}
.package__note{font-size:6.3px;color:var(--white);margin-top:2px}
.pill{position:absolute;height:26px;border-radius:8px 0 0 8px;color:var(--white);font-weight:300;font-style:italic;font-size:16px;padding-left:10px;display:flex;align-items:center}
.brand{position:absolute;left:325px;top:292px;display:flex;align-items:center;gap:7px;font-weight:700;font-size:17px;color:#2a2a2a}
.brand__dot{width:11px;height:11px;border-radius:50%;background:#c9a23a}
</style>
</head>
<body>
<div class="canvas">

  <section class="page options">
    <div class="options__top" role="img" aria-label="Soft faded photograph of a senior's hands in pastel tones"></div>
    <h1 class="options__title">EXTRA CHOICE OPTIONS</h1>

    <div class="option" style="top:70px">
      <svg viewBox="0 0 477 49" preserveAspectRatio="none"><rect width="477" height="49" fill="var(--violet)"/><polyline points="125,0 133,0 157,24.5 133,49 125,49" fill="none" stroke="#c4c6e0" stroke-width="2"/></svg>
      <div class="option__label">Centre Link / DVA Nominee<span class="option__price">$1,100</span></div>
      <div class="option__text">Communicate with CentreLink / DVA on behalf of our client/s, and undertake all changes and updates to details, as directed by our client.</div>
    </div>
    <div class="option" style="top:127px">
      <svg viewBox="0 0 477 49" preserveAspectRatio="none"><rect width="477" height="49" fill="var(--olive)"/><polyline points="125,0 133,0 157,24.5 133,49 125,49" fill="none" stroke="#c8c79a" stroke-width="2"/></svg>
      <div class="option__label">Post Implementation<br>Statement of Advice<span class="option__price">$1,650</span></div>
      <div class="option__text">Revise our original Advice Statement for any changes of circumstances including income &amp; asset variations, and provide further advice within the first 12 months of initial advice statement.</div>
    </div>
    <div class="option" style="top:184px">
      <svg viewBox="0 0 477 49" preserveAspectRatio="none"><rect width="477" height="49" fill="var(--violet)"/><polyline points="125,0 133,0 157,24.5 133,49 125,49" fill="none" stroke="#c4c6e0" stroke-width="2"/></svg>
      <div class="option__label">Annual Review<span class="option__price">$990</span></div>
      <div class="option__text">A review of the recommendations made in our original advice document, taking into account any changes to client's circumstances including checking current cash flow is sufficient to meet ongoing aged care costs.</div>
    </div>
    <div class="option" style="top:241px">
      <svg viewBox="0 0 477 49" preserveAspectRatio="none"><rect width="477" height="49" fill="var(--olive)"/><polyline points="125,0 133,0 157,24.5 133,49 125,49" fill="none" stroke="#c8c79a" stroke-width="2"/></svg>
      <div class="option__label">Post Entry Review<span class="option__price">$660</span></div>
      <div class="option__text">Review financial situation, check facility invoices are accurate, explain the Residential Aged Care Agreement and ensure all recommendations are implemented.</div>
    </div>
    <div class="option" style="top:298px">
      <svg viewBox="0 0 477 49" preserveAspectRatio="none"><rect width="477" height="49" fill="var(--violet)"/><polyline points="125,0 133,0 157,24.5 133,49 125,49" fill="none" stroke="#c4c6e0" stroke-width="2"/></svg>
      <div class="option__label">Facility Liason<span class="option__price">$550</span></div>
      <div class="option__text">Negotiate with the Aged Care Facility regarding Accommodation payments, clarify &amp; explain Residential Care Agreement, and review facility invoices.</div>
    </div>
    <div class="option" style="top:355px">
      <svg viewBox="0 0 477 49" preserveAspectRatio="none"><rect width="477" height="49" fill="var(--olive)"/><polyline points="125,0 133,0 157,24.5 133,49 125,49" fill="none" stroke="#c8c79a" stroke-width="2"/></svg>
      <div class="option__label">Family Conferences<span class="option__price">$660</span></div>
      <div class="option__text">Facilitate &amp; co-ordinate family meetings to explain the Aged Care legislation and how it fits with the family circumstances.</div>
    </div>
    <div class="option" style="top:412px">
      <svg viewBox="0 0 477 49" preserveAspectRatio="none"><rect width="477" height="49" fill="var(--violet)"/><polyline points="125,0 133,0 157,24.5 133,49 125,49" fill="none" stroke="#c4c6e0" stroke-width="2"/></svg>
      <div class="option__label">Family Conferences<span class="option__price">$660</span></div>
      <div class="option__text">Facilitate &amp; co-ordinate family meetings to explain the Aged Care legislation and how it fits with the family circumstances.</div>
    </div>

    <p class="signoff">I/We have chosen the Service Package and Options as ticked above. I/We understand that by choosing the Essentials Package, that I/We are receiving factual information only, and not financial advice. I/We agree to<br>pay the amount of ………………….., within seven days of the date of the invoice received from Harbourview Advisory.</p>
    <span class="dots" style="left:33px;top:530px">……………………………………………</span>
    <span class="dots" style="left:175px;top:530px">……………………………………………</span>
    <span class="dots" style="left:305px;top:530px">…………………………………………</span>
    <span class="dots" style="left:427px;top:530px">……./……../………</span>
    <span class="sig-row" style="left:72px;top:547px">Signature</span>
    <span class="sig-row" style="left:259px;top:547px">Signature Signature</span>
    <span class="sig-row" style="left:451px;top:547px">Date</span>
    <span class="dots" style="left:33px;top:570px">……………………………………………..</span>
    <span class="dots" style="left:173px;top:570px">………/………/………</span>
    <span class="sig-row" style="left:63px;top:587px">Adviser Signature</span>
    <span class="sig-row" style="left:208px;top:587px">Date</span>
    <div class="disclaimer">
      <p>This document has been prepared by Harbourview Advisory Pty Ltd ABN 00 000 000 001, an Authorised Representative of Northgate Wealth Limited ABN 00 000 000 002 AFSL 000000, a wholly owned, non-guaranteed subsidiary of the Southern Cross Banking Group ABN 00 000 000 003.</p>
      <p>Information in this document is based on current regulatory requirements and laws, as at 20 September, 2016 which may be subject to change. It contains general advice. It does not take into account your individual objectives, financial situation or needs. You should consider talking to a financial adviser before making a financial decision.</p>
    </div>
    <div class="options__foot"></div>
  </section>

  <section class="page packages">
    <svg class="packages__bg" viewBox="0 0 537 694" aria-hidden="true">
      <polygon points="0,304 262,304 350,392 0,392" fill="var(--violet-light)"/>
      <polygon points="0,392 378,392 338,432 0,432" fill="var(--grey-band)"/>
      <polygon points="0,432 338,432 300,470 300,478 263,540 0,540" fill="var(--olive)"/>
      <polygon points="0,540 263,540 270,547 0,547" fill="var(--olive)"/>
      <polygon points="0,547 270,547 300,585 0,585" fill="var(--grey-band)"/>
      <polygon points="0,585 300,585 390,694 0,694" fill="var(--violet)"/>
      <line x1="0" y1="302" x2="262" y2="302" stroke="var(--violet-deep)" stroke-width="1.5"/>
      <line x1="0" y1="433" x2="337" y2="433" stroke="var(--olive-dark)" stroke-width="1.5"/>
      <line x1="0" y1="586" x2="300" y2="586" stroke="var(--violet-deep)" stroke-width="1.5"/>
      <polygon points="537,278 537,694 400,694 274,547" fill="none" stroke="var(--cream)" stroke-width="7"/>
    </svg>
    <div class="photo" role="img" aria-label="Photograph of a smiling three-generation family sitting together on the grass" style="left:0;top:0;width:537px;height:264px;background:linear-gradient(160deg,#a9c27c 0%,#d9dcc0 40%,#c8b7a6 65%,#8aa55c 100%)"></div>
    <div class="photo" role="img" aria-label="Photograph of a young hand gently holding an elderly hand" style="left:0;top:0;width:537px;height:694px;clip-path:polygon(537px 288px,537px 694px,405px 694px,284px 547px);background:linear-gradient(200deg,#b59b8c 0%,#d8c2b0 45%,#9c8478 100%)"></div>

    <div class="brand"><span class="brand__dot"></span>Harbourview Advisory</div>

    <div class="package" style="top:268px">
      <div class="package__name">ESSENTIALS Package $770</div>
      <div class="package__tag">When you know what you want....</div>
      <ul class="package__list" style="margin-top:8px">
        <li>Explanation of Aged Care Fees and Charges.</li>
        <li>Preliminary Home / Assets Assessment.*</li>
        <li>Estimated Means Tested Fee Calculation.*</li>
        <li>Preliminary Aged Care Costs.*</li>
        <li>Estimated Cash Flow Scenario.*</li>
      </ul>
      <div class="package__note">*Please note this is general factual information only. We do not provide any specific personal information.</div>
    </div>
    <div class="pill" style="left:204px;top:344px;width:150px;background:var(--violet)">Peace of Mind</div>

    <div class="package" style="top:400px">
      <div class="package__name">ADVANTAGE Package $2,970</div>
      <div class="package__tag" style="color:#333">When you need to know all the options....</div>
      <div class="package__base" style="margin-top:6px">Essentials Package Plus</div>
      <ul class="package__list">
        <li>Analyse and Strategize Aged Care costs.</li>
        <li>Compare up to 5 Strategy options.</li>
        <li>Minimise Aged Care Costs (where possible).</li>
        <li>Maximise Age Pension Income (where possible).</li>
        <li>Prepare a Full Statement of Advice (SOA).</li>
        <li>Implementation of Aged Care Strategy.</li>
      </ul>
    </div>
    <div class="pill" style="left:204px;top:450px;width:140px;background:var(--olive-dark);opacity:.85">Confidence</div>

    <div class="package" style="top:553px">
      <div class="package__name">PLATINUM Package $5,940</div>
      <div class="package__tag">When you need someone to take charge</div>
      <div class="package__base" style="margin-top:6px">Advantage Packageplus</div>
      <ul class="package__list">
        <li>Liase with the Aged Care Facility.</li>
        <li>CentreLink/DVA Nominee.</li>
        <li>Post Entry Review.</li>
        <li>Post Implementation SOA (if required).</li>
        <li>Annual Review.</li>
      </ul>
    </div>
    <div class="pill" style="left:204px;top:606px;width:125px;background:var(--violet-light)">Convenience</div>
  </section>

</div>
</body>
</html>
```